Brivane LLC soda can design.

Welcome to Brivane luxury soda cans we offer five serious non sugar based flavors.

Soda, soda lime, soda green tea, soda tonic, soda ginger.

Plastic flag ship 750ml or 1l black label soda. Generic black label.
335 cans of same flag ship soda.

Thin tall 335 cans. Thin tall 250 cans. Normal 335 cans.

Files go to manufacturer for revision then back for final mastering.

Please center Image and scale all the same.

Pease be exact and consistent.

Transparent, white backgrounds for online selling and presentation.

Large gold font - Brivane tm
Small text - Established 2021 -
Small text with without copy.

Thank you.
Brivanellc@quenmail.com
Lumatrice@quenmail.com

Target Market(s)

Worldwide All ages generic soda

Industry/Entity Type

Soda water

Font styles to use
Serif
Decorative

Requirements
Must have
• Revisions after post manufacturer approval.
Nice to have
• 48706927 design generic soda
Should not have
• Non generic

```html
<!DOCTYPE html>
<html lang="en">
<head>
<meta charset="utf-8">
<title>Brivane Soda Label</title>
<link rel="stylesheet" href="https://fonts.googleapis.com/css2?family=Bodoni+Moda:wght@500&family=Montserrat:wght@400;600&display=swap">
<style>
  :root {
    --canvas: #ffffff;
    --label-black: #1c1c1c;
    --label-deep: #111111;
    --line-grey: #3a3a3a;
    --gold: #c9b27a;
    --silver: #b9bcc0;
    --text-light: #e6e6e6;
  }
  html, body {
    margin: 0;
    padding: 0;
    overflow: hidden;
  }
  body {
    width: 900px;
    height: 1200px;
    background: var(--canvas);
    position: relative;
    font-family: "Montserrat", sans-serif;
  }
  .neck-label {
    position: absolute;
    left: 330px;
    top: 90px;
    width: 240px;
    height: 260px;
    background: var(--label-black);
    border-bottom: 10px solid var(--silver);
    display: flex;
    align-items: center;
    justify-content: center;
  }
  .neck-mark {
    display: flex;
    align-items: center;
    gap: 10px;
  }
  .neck-dot {
    width: 18px;
    height: 18px;
    border: 2px solid var(--gold);
    border-radius: 50%;
  }
  .neck-name {
    font-family: "Bodoni Moda", serif;
    font-weight: 500;
    font-size: 30px;
    color: var(--gold);
    letter-spacing: 1px;
  }
  .body-label {
    position: absolute;
    left: 50px;
    top: 440px;
    width: 800px;
    height: 470px;
    overflow: hidden;
  }
  .body-label__pattern {
    position: absolute;
    inset: 0;
    background: linear-gradient(170deg, var(--label-black) 0%, #262626 45%, var(--label-deep) 100%);
  }
  .body-label__content {
    position: absolute;
    inset: 0;
    display: flex;
    flex-direction: column;
    align-items: center;
    padding-top: 158px;
    box-sizing: border-box;
  }
  .brand-name {
    font-family: "Bodoni Moda", serif;
    font-weight: 500;
    font-size: 124px;
    line-height: 1;
    color: var(--gold);
    letter-spacing: -2px;
    text-transform: uppercase;
  }
  .established {
    margin-top: 14px;
    font-size: 22px;
    color: var(--text-light);
    letter-spacing: 0.5px;
  }
  .flavour {
    margin-top: 42px;
    font-size: 26px;
    font-weight: 600;
    color: #ffffff;
    letter-spacing: 1px;
  }
  .volume {
    margin-top: 4px;
    font-size: 28px;
    color: var(--text-light);
  }
</style>
</head>
<body>
  <div class="neck-label">
    <div class="neck-mark">
      <span class="neck-dot"></span>
      <span class="neck-name">Brivane</span>
    </div>
  </div>

  <section class="body-label">
    <div class="body-label__pattern" role="img" aria-label="Fine grey wave lines flowing across the black label"></div>
    <div class="body-label__content">
      <div class="brand-name">Brivane</div>
      <div class="established">Established 2021</div>
      <div class="flavour">SODA</div>
      <div class="volume">750ml</div>
    </div>
  </section>
</body>
</html>
```